Anzeigengestaltung für Fliesenlegermeister
Zielgruppe
Ich bin ein Fliesenlegermeister und möchte mich selbstständig machen, ich saniere Bäder, Böden mit Fliesen, Fliesenspiegel und ich möchte eine Anzeige in den regionalen Zeitungen machen. Ich spreche alle Altersklassen mit Bädern für Sanierungen, Bodenfliesen und Neubauten an. Reparatur und Silikonarbeiten sowie Trockenbauarbeiten am eigenen Heim .
Aufgabenstellung
Ich möchte gern meine Kontaktdaten und die Farben vom Logo wieder finden,
als Beispiel habe ich meine aktuelle Visitenkarte beigefügt Dort finden sich die Kontaktdaten. Meine Arbeiten sind insbesondere :
Fliesenverlegung
Badsanierung
barrierefreie Bäder
Reparaturarbeiten
Silikonarbeiten
Trockenbau
Ob nun genau alle 6 Punkte in der Anzeige angezeigt werden soll bin ich mir nicht sicher oder ob nur 4 Beschreibungen reichen, damit es nicht zu viel wird.

```html
<!DOCTYPE html>
<html lang="de">
<head>
<meta charset="utf-8">
<title>Anzeige Fliesenlegermeister</title>
<link rel="stylesheet" href="https://fonts.googleapis.com/css2?family=Kaushan+Script&family=Montserrat:wght@500;700&family=Open+Sans:wght@400;600&display=swap">
<style>
  :root {
    --brand-blue: #0f57a3;
    --ink: #222428;
    --slate: #4a4d52;
    --paper: #ffffff;
    --backdrop: #e4e5e6;
  }
  * { box-sizing: border-box; margin: 0; padding: 0; }
  html, body { width: 1200px; height: 803px; overflow: hidden; }
  body {
    background: var(--backdrop);
    display: flex;
    align-items: center;
    justify-content: center;
  }
  .ad {
    width: 580px;
    height: 700px;
    background: var(--paper);
    display: flex;
    flex-direction: column;
    box-shadow: 0 2px 10px rgba(0,0,0,.08);
  }
  .ad-main {
    flex: 1;
    padding: 44px 44px 0 46px;
    position: relative;
  }
  .corner-square {
    position: absolute;
    top: 30px;
    right: 36px;
    width: 74px;
    height: 74px;
    background: var(--brand-blue);
    transform: rotate(45deg);
  }
  .headline {
    font-family: "Kaushan Script", cursive;
    font-size: 40px;
    line-height: 1.2;
    color: var(--slate);
    transform: rotate(-4deg);
    transform-origin: left top;
    margin-bottom: 40px;
  }
  .headline .accent { color: var(--brand-blue); }
  .services {
    list-style: none;
    font-family: "Open Sans", sans-serif;
    font-weight: 600;
    font-size: 25px;
    color: var(--ink);
  }
  .services li {
    display: flex;
    align-items: center;
    gap: 14px;
    margin-bottom: 12px;
  }
  .services svg { width: 22px; height: 22px; flex: none; }
  .brand {
    display: flex;
    align-items: center;
    gap: 18px;
    margin-top: 46px;
    margin-left: 40px;
  }
  .brand-square {
    width: 46px;
    height: 46px;
    background: var(--slate);
  }
  .brand-name {
    font-family: "Montserrat", sans-serif;
    font-weight: 700;
    font-size: 36px;
    letter-spacing: 1px;
    text-transform: uppercase;
    color: var(--brand-blue);
  }
  .contact {
    background: var(--brand-blue);
    height: 230px;
    padding: 28px 50px;
    list-style: none;
    font-family: "Open Sans", sans-serif;
    font-size: 20px;
    color: var(--paper);
  }
  .contact li {
    display: flex;
    align-items: flex-start;
    gap: 22px;
    margin-bottom: 10px;
    line-height: 1.25;
  }
  .contact svg {
    width: 30px; height: 30px; flex: none;
  }
</style>
</head>
<body>
  <article class="ad">
    <section class="ad-main">
      <div class="corner-square"></div>
      <h1 class="headline">Ihr <span class="accent">Fliesenleger</span> aus<br>Braunschweig</h1>
      <ul class="services">
        <li><svg viewBox="0 0 22 22"><path d="M3 11l5 6L19 4" fill="none" stroke="#0f57a3" stroke-width="3.5" stroke-linecap="round" stroke-linejoin="round"/></svg>Fliesenverlegung</li>
        <li><svg viewBox="0 0 22 22"><path d="M3 11l5 6L19 4" fill="none" stroke="#0f57a3" stroke-width="3.5" stroke-linecap="round" stroke-linejoin="round"/></svg>Badsanierung</li>
        <li><svg viewBox="0 0 22 22"><path d="M3 11l5 6L19 4" fill="none" stroke="#0f57a3" stroke-width="3.5" stroke-linecap="round" stroke-linejoin="round"/></svg>barrierefreie Bäder</li>
        <li><svg viewBox="0 0 22 22"><path d="M3 11l5 6L19 4" fill="none" stroke="#0f57a3" stroke-width="3.5" stroke-linecap="round" stroke-linejoin="round"/></svg>Reparaturarbeiten</li>
      </ul>
      <div class="brand">
        <div class="brand-square"></div>
        <span class="brand-name">Jonas Hartwig</span>
      </div>
    </section>
    <ul class="contact">
      <li>
        <svg viewBox="0 0 30 30"><rect x="2" y="2" width="26" height="26" fill="none" stroke="#fff" stroke-width="2"/><path d="M10 8l3 3-2 2c1 2 3 4 5 5l2-2 3 3-2 3c-5 0-11-6-11-11z" fill="none" stroke="#fff" stroke-width="1.6" stroke-linejoin="round"/></svg>
        <span>0531/4471920</span>
      </li>
      <li>
        <svg viewBox="0 0 30 30"><rect x="2" y="2" width="26" height="26" fill="none" stroke="#fff" stroke-width="2"/><rect x="8" y="10" width="14" height="10" fill="none" stroke="#fff" stroke-width="1.6"/><path d="M8 10l7 6 7-6" fill="none" stroke="#fff" stroke-width="1.6"/></svg>
        <span>info@fliesenleger-hartwig.de</span>
      </li>
      <li>
        <svg viewBox="0 0 30 30"><rect x="2" y="2" width="26" height="26" fill="none" stroke="#fff" stroke-width="2"/><path d="M15 23s-6-6-6-10a6 6 0 0 1 12 0c0 4-6 10-6 10z" fill="none" stroke="#fff" stroke-width="1.6"/><circle cx="15" cy="13" r="2" fill="#fff"/></svg>
        <span>Lindenweg 7,<br>38100 Braunschweig</span>
      </li>
      <li>
        <svg viewBox="0 0 30 30"><rect x="2" y="2" width="26" height="26" fill="none" stroke="#fff" stroke-width="2"/><circle cx="15" cy="15" r="7" fill="none" stroke="#fff" stroke-width="1.6"/><ellipse cx="15" cy="15" rx="3" ry="7" fill="none" stroke="#fff" stroke-width="1.4"/><path d="M8 15h14" stroke="#fff" stroke-width="1.4"/></svg>
        <span>www.fliesenleger-hartwig.de</span>
      </li>
    </ul>
  </article>
</body>
</html>
```